harborline slab pumping "just pump it"

I want very easy to understand cards that say everything we offer.
i want the company name/logo, phone number and email on the front of card.
i want the card to stand out, it can be red with black lettering.
on the back of the card i want it to list everything that we can do like a list
the motto is JUST PUMP IT.
the can be in the lower right corner of the back of the card

Target Market(s)

concrete contractors

Industry/Entity Type

Concrete

Contact Information for Business Card

back of the card
Owner:Marco Tellin
Phone:503)418-6093
Email: HSPumping@slabmail.example
address: 22816 se brindle ave Portland, OR 97236

Colors
ec1f27
000000
959595
5c5c5c
f04a50
ffffff
f37122

Requirements
Must have
• :we have years of experience in the world of concrete
• :our pumps can do up to 70 yards an hour
• :if you refer us to other contractors, will give you up to 10% off next pump job
• :don’t hesitate to call if you have any concrete related questions and to get a qoute
• Please put this on the front of the card, “just pump it” in the lower right corner

```html
<!DOCTYPE html>
<html lang="en">
<head>
<meta charset="utf-8">
<title>Harborline Slab Pumping – Business Cards</title>
<link href="https://fonts.googleapis.com/css2?family=Montserrat:wght@400;600;700&family=Roboto:wght@400;500;700&display=swap" rel="stylesheet">
<style>
  :root{
    --stage:#1c1c1c;
    --card-front:#545454;
    --card-back:#3b3b3b;
    --map-light:#6a6a6a;
    --map-dark:#474747;
    --red:#ec1f27;
    --white:#ffffff;
    --soft-white:#e6e6e6;
    --rule:#959595;
  }
  *{box-sizing:border-box;margin:0;padding:0}
  html,body{width:1200px;height:900px;overflow:hidden;background:var(--stage)}
  .canvas{position:relative;width:1200px;height:900px}
  .card{position:absolute;left:300px;width:600px;height:343px;overflow:hidden}
  .card--front{top:80px;background:var(--card-front)}
  .card--back{top:467px;background:var(--card-back)}
  .map-field{position:absolute;inset:30px 40px 60px 40px;border-radius:40px;opacity:.45}
  .card--front .map-field{background:radial-gradient(ellipse at center,var(--map-light),transparent 70%)}
  .card--back .map-field{background:radial-gradient(ellipse at center,var(--map-dark),transparent 70%);opacity:.8}

  .brand{position:absolute;display:flex;align-items:center;gap:14px;font-family:"Montserrat",sans-serif}
  .brand__dot{width:58px;height:58px;border-radius:50%;flex:none}
  .brand__name{font-weight:700;line-height:1.05;letter-spacing:1px;text-transform:uppercase;white-space:nowrap}
  .brand__phone{font-weight:600;margin-top:6px;white-space:nowrap}

  .card--front .brand{left:50%;top:58px;transform:translateX(-50%)}
  .card--front .brand__dot{background:var(--white)}
  .card--front .brand__name{color:var(--white);font-size:24px}
  .card--front .brand__phone{color:var(--white);font-size:18px;letter-spacing:6px}

  .services{position:absolute;left:70px;right:70px;top:160px;list-style:none;font-family:"Montserrat",sans-serif;font-size:11.5px;line-height:1.35;color:var(--white)}
  .services li{display:flex;gap:8px;margin-bottom:7px}
  .services li::before{content:"";flex:none;width:6px;height:6px;margin-top:5px;background:var(--red)}
  .front__motto{position:absolute;right:26px;bottom:20px;font-family:"Montserrat",sans-serif;font-weight:700;font-size:16px;letter-spacing:2px;color:var(--red);text-transform:uppercase}

  .card--back .brand{left:34px;top:128px}
  .card--back .brand__dot{background:var(--red);width:50px;height:50px}
  .card--back .brand__name{color:var(--red);font-size:22px}
  .card--back .brand__phone{color:var(--white);font-size:16px;letter-spacing:4px}
  .back__divider{position:absolute;left:352px;top:84px;width:1px;height:120px;background:var(--rule)}
  .person{position:absolute;left:370px;top:84px;font-family:"Roboto",sans-serif;color:var(--white)}
  .person__name{font-family:"Montserrat",sans-serif;font-weight:700;font-size:24px;letter-spacing:1px;text-transform:uppercase}
  .person__title{font-size:13px;color:var(--soft-white);margin-top:2px}
  .contact{list-style:none;margin-top:14px;font-size:13px;color:var(--soft-white)}
  .contact li{display:flex;align-items:center;gap:8px;margin-bottom:5px;white-space:nowrap}
  .contact svg{width:11px;height:11px;flex:none}
  .band-line{position:absolute;left:0;right:0;bottom:54px;height:2px;background:var(--red)}
  .band{position:absolute;left:0;right:0;bottom:0;height:48px;background:var(--red);display:flex;align-items:center;justify-content:center;font-family:"Roboto",sans-serif;font-size:14px;color:var(--white)}
</style>
</head>
<body>
<main class="canvas">
  <section class="card card--front">
    <div class="map-field" role="img" aria-label="Faint dotted world map background"></div>
    <div class="brand">
      <span class="brand__dot"></span>
      <div>
        <p class="brand__name">Harborline Slab Pumping</p>
        <p class="brand__phone">(503)418-6093</p>
      </div>
    </div>
    <ul class="services">
      <li>We have years of experience in the world of concrete</li>
      <li>Our pumps can do up to 70 yards an hour</li>
      <li>Refer us to other contractors and get up to 10% off your next pump job</li>
      <li>Don't hesitate to call with any concrete related questions and to get a quote</li>
    </ul>
    <p class="front__motto">Just Pump It</p>
  </section>

  <section class="card card--back">
    <div class="map-field" role="img" aria-label="Faint dotted world map background"></div>
    <div class="brand">
      <span class="brand__dot"></span>
      <div>
        <p class="brand__name">Harborline<br>Slab Pumping</p>
        <p class="brand__phone">(503)418-6093</p>
      </div>
    </div>
    <div class="back__divider"></div>
    <div class="person">
      <p class="person__name">Marco Tellin</p>
      <p class="person__title">Design Consultant</p>
      <ul class="contact">
        <li><svg viewBox="0 0 12 12"><rect x="3" y="0.5" width="6" height="11" rx="1" fill="none" stroke="#ec1f27" stroke-width="1.2"/></svg>503)418-6093</li>
        <li><svg viewBox="0 0 12 12"><rect x="0.6" y="2" width="10.8" height="8" fill="none" stroke="#ec1f27" stroke-width="1.2"/><path d="M1 2.5 6 6.5 11 2.5" fill="none" stroke="#ec1f27" stroke-width="1.2"/></svg>HSPumping@slabmail.example</li>
        <li><svg viewBox="0 0 12 12"><circle cx="6" cy="6" r="5" fill="none" stroke="#ec1f27" stroke-width="1.2"/><path d="M1 6h10M6 1c-2.5 3-2.5 7 0 10M6 1c2.5 3 2.5 7 0 10" fill="none" stroke="#ec1f27" stroke-width="1"/></svg>harborlineslabpumping.example</li>
      </ul>
    </div>
    <div class="band-line"></div>
    <p class="band">22816 se brindle ave Portland, OR 97236</p>
  </section>
</main>
</body>
</html>
```